Business card for medical clinic

I need an upmarket, modern medical/health business card for my clinic

Contact Information for Business Card

name, address, email, qr code

```html
<!DOCTYPE html>
<html lang="en">
<head>
<meta charset="utf-8">
<title>Brelvane Health Collective – Business Card</title>
<link rel="stylesheet" href="https://fonts.googleapis.com/css2?family=Poppins:wght@300;400;500;700&display=swap">
<style>
  :root{
    --page:#222222;
    --paper:#ffffff;
    --brand-blue:#1e9ad6;
    --brand-navy:#1c2a4a;
    --deep-blue:#17609a;
    --ink:#151515;
    --rule:#3a8fcf;
  }
  *{box-sizing:border-box;margin:0;padding:0}
  html,body{width:1200px;height:780px;overflow:hidden;background:var(--page)}
  body{font-family:"Poppins",sans-serif;position:relative}

  .card{
    position:absolute;top:235px;width:540px;height:310px;
    border-radius:3px;overflow:hidden;
    box-shadow:0 18px 40px rgba(0,0,0,.55);
  }
  .card--front{left:40px;background:var(--paper)}
  .card--back{
    left:620px;
    background:linear-gradient(225deg,var(--brand-navy) 0%,#1f4e7e 28%,#1a86c4 55%,#22a6e0 78%,#1e98d4 100%);
  }

  /* wordmark */
  .wordmark{position:absolute;display:flex;align-items:center;gap:12px}
  .wordmark__dot{border-radius:50%;flex:none}
  .wordmark__name{font-weight:500;letter-spacing:.08em;text-transform:uppercase;line-height:1.2;white-space:nowrap}

  .card--front .wordmark{left:36px;top:40px}
  .card--front .wordmark__dot{width:46px;height:46px;border:3px solid var(--brand-blue)}
  .card--front .wordmark__name{font-size:16px;color:var(--deep-blue)}

  .card--back .wordmark{left:50%;top:50%;transform:translate(-50%,-50%);gap:20px}
  .card--back .wordmark__dot{width:86px;height:86px;border:4px solid #fff}
  .card--back .wordmark__name{font-size:27px;color:#fff}

  .divider{position:absolute;left:262px;top:98px;width:1px;height:150px;background:var(--rule)}

  .contact{position:absolute;left:292px;top:104px}
  .contact__name{font-size:28px;line-height:1;color:var(--brand-blue);white-space:nowrap}
  .contact__first{font-weight:700}
  .contact__last{font-weight:300}
  .contact__role{font-size:12.5px;font-weight:500;color:var(--ink);margin-top:6px}
  .contact__list{list-style:none;margin-top:12px}
  .contact__item{display:flex;align-items:center;gap:9px;font-size:13px;color:var(--ink);line-height:1.7;white-space:nowrap}
  .contact__icon{width:12px;height:12px;flex:none;fill:var(--brand-blue)}

  .address{position:absolute;left:36px;bottom:30px;font-size:13px;color:var(--brand-blue);white-space:nowrap}
</style>
</head>
<body>

<section class="card card--front" aria-label="Card front">
  <div class="wordmark">
    <span class="wordmark__dot"></span>
    <span class="wordmark__name">Brelvane Health<br>Collective</span>
  </div>

  <div class="divider"></div>

  <div class="contact">
    <p class="contact__name"><span class="contact__first">Marta</span> <span class="contact__last">Kovalen</span></p>
    <p class="contact__role">Founder &amp; CEO</p>
    <ul class="contact__list">
      <li class="contact__item">
        <svg class="contact__icon" viewBox="0 0 24 24" aria-hidden="true"><path d="M6.6 10.8a15.1 15.1 0 0 0 6.6 6.6l2.2-2.2c.3-.3.7-.4 1-.2 1.1.4 2.3.6 3.6.6.6 0 1 .4 1 1V20c0 .6-.4 1-1 1A17 17 0 0 1 3 4c0-.6.4-1 1-1h3.5c.6 0 1 .4 1 1 0 1.3.2 2.5.6 3.6.1.3 0 .7-.2 1z"/></svg>
        (555) 214-0386
      </li>
      <li class="contact__item">
        <svg class="contact__icon" viewBox="0 0 24 24" aria-hidden="true"><path d="M12 2a10 10 0 1 0 0 20 10 10 0 0 0 0-20zm6.9 6h-3a15.6 15.6 0 0 0-1.3-3.6A8 8 0 0 1 18.9 8zM12 4c.8 1.2 1.5 2.5 1.9 4h-3.8c.4-1.5 1.1-2.8 1.9-4zM4.3 14a8.2 8.2 0 0 1 0-4h3.4a16 16 0 0 0 0 4zm.8 2h3a15.6 15.6 0 0 0 1.3 3.6A8 8 0 0 1 5.1 16zm3-8h-3a8 8 0 0 1 4.3-3.6C8.8 5.5 8.4 6.7 8.1 8zM12 20c-.8-1.2-1.5-2.5-1.9-4h3.8c-.4 1.5-1.1 2.8-1.9 4zm2.3-6H9.7a14.7 14.7 0 0 1 0-4h4.6a14.7 14.7 0 0 1 0 4zm.3 5.6c.6-1.1 1-2.3 1.3-3.6h3a8 8 0 0 1-4.3 3.6zm1.7-5.6a16 16 0 0 0 0-4h3.4a8.2 8.2 0 0 1 0 4z"/></svg>
        info@brelvanehealth.com
      </li>
      <li class="contact__item">
        <svg class="contact__icon" viewBox="0 0 24 24" aria-hidden="true"><path d="M3 5h18c.6 0 1 .4 1 1v12c0 .6-.4 1-1 1H3c-.6 0-1-.4-1-1V6c0-.6.4-1 1-1zm1 2.4V17h16V7.4l-8 5.3z M5 7l7 4.6L19 7z"/></svg>
        www.brelvanehealth.com
      </li>
    </ul>
  </div>

  <p class="address">1840 Linden Ave. Suite 300 Brookfield, TX 75010</p>
</section>

<section class="card card--back" aria-label="Card back">
  <div class="wordmark">
    <span class="wordmark__dot"></span>
    <span class="wordmark__name">Brelvane Health<br>Collective</span>
  </div>
</section>

</body>
</html>
```